Drovane Supplies Ltd Stationery Design Project

hi we need to design business cards, letter head, complimentary slips, scribble pads, note pads, envelopes for drovane supplies ltd.

please see business cards details

Kelwin Osterby

P.O Box 43817 -00291 Nairobi - Kenya
Tel: +254-733-281-914
Email: drovanesupplies@mailvaro.example

company name should appear on all stationery : Drovane Supplies Ltd

Industry/Entity Type

Business

Requirements
Must have
• kindly stick to colours in the logo

```html
<!DOCTYPE html>
<html lang="en">
<head>
<meta charset="utf-8">
<title>Drovane Supplies Ltd — Stationery</title>
<link rel="stylesheet" href="https://fonts.googleapis.com/css2?family=Michroma&family=Saira+Semi+Condensed:wght@400;600&display=swap">
<style>
  :root {
    --bg: #e6e6e8;
    --paper: #ffffff;
    --orange: #f0931e;
    --blue: #2b3590;
    --ink: #3a3a3a;
    --ghost: #dcdcdc;
    --sun-orange: #f6b25a;
    --shadow: 0 6px 18px rgba(0,0,0,.18);
  }
  * { box-sizing: border-box; margin: 0; padding: 0; }
  html, body { width: 1200px; height: 958px; overflow: hidden; }
  body { background: var(--bg); position: relative; font-family: "Saira Semi Condensed", sans-serif; }

  .sheet { position: absolute; background: var(--paper); box-shadow: var(--shadow); overflow: hidden; }

  .ornament { position: absolute; border-radius: 50%; }
  .ornament--orange { background: radial-gradient(circle, var(--sun-orange) 0%, rgba(246,178,90,.35) 70%, rgba(246,178,90,0) 72%); }
  .ornament--ghost { background: radial-gradient(circle, var(--ghost) 0%, rgba(220,220,220,.45) 70%, rgba(220,220,220,0) 72%); }

  .brand { display: flex; align-items: center; gap: 10px; position: absolute; }
  .brand__name { font-family: "Michroma", sans-serif; color: var(--blue); line-height: 1.15; text-transform: uppercase; }
  .brand__rule { width: 1px; background: var(--ink); align-self: stretch; }
  .contact { font-size: 8px; line-height: 1.45; color: var(--ink); font-weight: 600; white-space: nowrap; }
  .contact__email { color: var(--orange); }

  /* Letterhead */
  .letterhead { left: 60px; top: 60px; width: 560px; height: 792px; }
  .letterhead .ornament--top { left: 225px; top: -55px; width: 100px; height: 100px; }
  .letterhead .ornament--bottom { left: 155px; top: 655px; width: 275px; height: 275px; }
  .letterhead__mark { position: absolute; left: 0; top: 148px; width: 14px; height: 30px; background: var(--orange); }
  .letterhead .brand { left: 22px; top: 140px; }
  .letterhead .brand__name { font-size: 13px; width: 110px; }
  .letterhead__band { position: absolute; left: 390px; right: 0; top: 150px; height: 28px; background: var(--blue); }

  /* Envelope */
  .envelope { left: 660px; top: 150px; width: 500px; height: 250px; }
  .envelope .ornament--left { left: -95px; top: 20px; width: 200px; height: 200px; }
  .envelope .ornament--right { left: 450px; top: 75px; width: 110px; height: 110px; }
  .envelope .brand { left: 130px; top: 100px; }
  .envelope .brand__name { font-size: 14px; width: 112px; }

  /* Business card */
  .card { left: 660px; top: 460px; width: 380px; height: 228px; }
  .card .ornament--left { left: -80px; top: 10px; width: 170px; height: 170px; }
  .card .ornament--right { left: 345px; top: 20px; width: 70px; height: 70px; }
  .card .brand { left: 120px; top: 80px; }
  .card .brand__name { font-size: 14px; width: 120px; }
  .card__person { position: absolute; left: 120px; top: 140px; font-size: 9px; font-weight: 600; color: var(--blue); text-transform: uppercase; letter-spacing: .5px; }
  .card .contact { position: absolute; left: 120px; top: 165px; }
</style>
</head>
<body>

<section class="sheet letterhead" aria-label="Letterhead">
  <div class="ornament ornament--orange ornament--top" role="img" aria-label="Orange sun ornament"></div>
  <div class="letterhead__mark"></div>
  <div class="brand">
    <span class="brand__name">Drovane Supplies Ltd</span>
    <span class="brand__rule"></span>
    <p class="contact">P.O Box 43817 -00291 Nairobi - Kenya<br>Tel: +254-733-281-914<br><span class="contact__email">Email: drovanesupplies@mailvaro.example</span></p>
  </div>
  <div class="letterhead__band"></div>
  <div class="ornament ornament--ghost ornament--bottom" role="img" aria-label="Faint grey sun ornament"></div>
</section>

<section class="sheet envelope" aria-label="Envelope">
  <div class="ornament ornament--ghost ornament--left" role="img" aria-label="Faint grey sun ornament"></div>
  <div class="brand">
    <span class="brand__name">Drovane Supplies Ltd</span>
    <span class="brand__rule"></span>
    <p class="contact">P.O Box 43817 -00291 Nairobi - Kenya<br>Tel: +254-733-281-914<br><span class="contact__email">Email: drovanesupplies@mailvaro.example</span></p>
  </div>
  <div class="ornament ornament--orange ornament--right" role="img" aria-label="Orange sun ornament"></div>
</section>

<section class="sheet card" aria-label="Business card">
  <div class="ornament ornament--ghost ornament--left" role="img" aria-label="Faint grey sun ornament"></div>
  <div class="brand">
    <span class="brand__name">Drovane Supplies Ltd</span>
  </div>
  <p class="card__person">Kelwin Osterby</p>
  <p class="contact">P.O Box 43817 -00291 Nairobi - Kenya<br>Tel: +254-733-281-914<br><span class="contact__email">drovanesupplies@mailvaro.example</span></p>
  <div class="ornament ornament--orange ornament--right" role="img" aria-label="Orange sun ornament"></div>
</section>

</body>
</html>
```